2 Creative Website Banners for Furniture Brand

Morning Davoskel....
The get a great night sleep banner is complete - we are happy with that one.
Ive uploaded a slightly different concept for the other banner below. This is just something rough ive thrown together. But you can see I have added a curve, a maroon coloured background which is slightly transparent and a big heart in the background....
I do not necessarily want to use this heart image but something a bit like this (a nice graphic, gif etc) but something quite elegant faded in, or perhaps a number of hearts (done in a tasteful way). Also can we keep the typography in the same format as you can see for this one.
Nearly there :)!
Industry/Entity Type
Furniture

```html
<!DOCTYPE html>
<html lang="en">
<head>
<meta charset="utf-8">
<title>Marlowe Furniture – Find a Look You Love</title>
<link rel="stylesheet" href="https://fonts.googleapis.com/css2?family=Archivo+Black&family=Josefin+Sans:wght@300;400&family=Open+Sans:wght@400;600&display=swap">
<style>
  :root {
    --sand: #e3d8c6;
    --sand-text: #978663;
    --taupe: #a08c80;
    --plum: #3a1f3d;
    --ink: #231a26;
    --gold: #cdb23d;
    --white: #ffffff;
    --button-text: #9b8b7b;
    --maroon-veil: rgba(96, 26, 52, 0.55);
    --heart-glow: rgba(255, 220, 230, 0.10);
    --photo-dark: #1d1b1f;
    --photo-mid: #3a3439;
    --photo-light: #5c5058;
  }
  * { box-sizing: border-box; margin: 0; padding: 0; }
  html, body { width: 1200px; height: 518px; overflow: hidden; background: var(--white); }
  .page { position: relative; width: 1200px; height: 518px; font-family: "Open Sans", sans-serif; }

  .notice-bar {
    position: absolute; top: 0; left: 0; width: 100%; height: 24px;
    background: var(--sand); color: var(--sand-text);
    font-size: 10.5px; letter-spacing: 0.2px;
    display: flex; align-items: center; justify-content: center;
  }

  .site-header { position: absolute; top: 24px; left: 0; width: 100%; height: 96px; background: var(--white); }
  .brand {
    position: absolute; left: 49px; top: 27px; width: 205px;
    font-family: "Josefin Sans", sans-serif; font-weight: 400;
    color: var(--plum); text-align: center; line-height: 1;
  }
  .brand-name { display: block; font-size: 29px; letter-spacing: 5px; margin-right: -5px; }
  .brand-sub { display: block; font-size: 9px; letter-spacing: 2.5px; margin-top: 4px; }

  .phone {
    position: absolute; right: 56px; top: 12px;
    display: flex; align-items: center; gap: 10px;
    font-size: 25px; color: var(--ink); letter-spacing: 0.5px;
  }
  .phone svg { width: 24px; height: 24px; }

  .account-links {
    position: absolute; right: 62px; top: 62px;
    display: flex; gap: 20px; list-style: none;
    font-size: 11.5px; color: var(--ink);
  }
  .account-links li { display: flex; align-items: center; gap: 5px; }
  .account-links svg { width: 16px; height: 16px; }
  .cart-count { color: var(--gold); margin-left: 4px; }

  .main-nav {
    position: absolute; top: 120px; left: 0; width: 100%; height: 43px;
    background: var(--taupe);
  }
  .main-nav ul { list-style: none; position: relative; height: 100%; }
  .main-nav li {
    position: absolute; top: 0; height: 100%;
    display: flex; align-items: center; gap: 8px;
    color: var(--white); font-size: 14.5px; transform: translateX(-50%);
  }
  .main-nav svg { width: 10px; height: 10px; }

  .hero { position: absolute; top: 163px; left: 0; width: 100%; height: 355px; overflow: hidden; }
  .hero-photo-left {
    position: absolute; left: 0; top: 0; width: 620px; height: 100%;
    background: linear-gradient(100deg, var(--photo-dark) 0%, #262327 60%, #2d2a2f 100%);
  }
  .hero-photo-right {
    position: absolute; left: 620px; top: 0; width: 580px; height: 100%;
    background: radial-gradient(ellipse at 45% 65%, #8a7c86 0%, var(--photo-light) 35%, var(--photo-mid) 70%, #262227 100%);
  }
  .hero-veil { position: absolute; left: 0; top: 0; width: 1200px; height: 355px; }

  .hero-copy { position: absolute; left: 0; top: 0; width: 624px; height: 100%; }
  .hero-kicker {
    position: absolute; left: 169px; top: 62px; white-space: nowrap;
    font-family: "Josefin Sans", sans-serif; font-weight: 300;
    font-size: 43px; color: var(--white); line-height: 1;
  }
  .hero-title {
    position: absolute; left: 213px; top: 112px;
    font-family: "Archivo Black", sans-serif; font-size: 76px;
    color: var(--sand); line-height: 1; letter-spacing: -1px;
  }
  .hero-text {
    position: absolute; left: 162px; top: 201px; width: 300px; text-align: center;
    font-family: "Josefin Sans", sans-serif; font-weight: 300; font-size: 15px;
    line-height: 16px; color: var(--white);
  }
  .hero-button {
    position: absolute; left: 215px; top: 255px; width: 195px; height: 36px;
    background: var(--sand); color: var(--button-text);
    font-size: 19px; display: flex; align-items: center; justify-content: center;
  }
</style>
</head>
<body>
<div class="page">
  <div class="notice-bar">COVID 19 - WE ARE TAKING ORDERS AND DELIVERING AS NORMAL</div>

  <header class="site-header">
    <div class="brand">
      <span class="brand-name">MARLOWE</span>
      <span class="brand-sub">FURNITURE</span>
    </div>

    <div class="phone">
      <svg viewBox="0 0 24 24" aria-hidden="true">
        <circle cx="12" cy="12" r="11" fill="#22357a"/>
        <rect x="9.5" y="1" width="5" height="22" fill="#fff"/>
        <rect x="1" y="9.5" width="22" height="5" fill="#fff"/>
        <rect x="10.7" y="1" width="2.6" height="22" fill="#c8202f"/>
        <rect x="1" y="10.7" width="22" height="2.6" fill="#c8202f"/>
      </svg>
      <span>0345 210 7788</span>
    </div>

    <ul class="account-links">
      <li>
        <svg viewBox="0 0 16 16" aria-hidden="true"><circle cx="8" cy="8" r="6.5" fill="none" stroke="var(--gold)" stroke-width="1.8"/></svg>
        TRACK ORDER
      </li>
      <li>
        <svg viewBox="0 0 16 16" aria-hidden="true"><path d="M8 14 L2 8 A3.3 3.3 0 0 1 8 3.6 A3.3 3.3 0 0 1 14 8 Z" fill="var(--gold)"/></svg>
        MY WISHLIST
      </li>
      <li>
        <svg viewBox="0 0 16 16" aria-hidden="true"><rect x="2.5" y="5" width="11" height="10" fill="none" stroke="var(--gold)" stroke-width="1.5"/><path d="M5.5 5 V3.5 A2.5 2.5 0 0 1 10.5 3.5 V5" fill="none" stroke="var(--gold)" stroke-width="1.5"/></svg>
        CART <span class="cart-count">( )</span>
      </li>
    </ul>
  </header>

  <nav class="main-nav">
    <ul>
      <li style="left:169px">HOME</li>
      <li style="left:347px">BEDROOM <svg viewBox="0 0 10 10" aria-hidden="true"><path d="M1.5 3 L5 6.5 L8.5 3" fill="none" stroke="#fff" stroke-width="1.6"/></svg></li>
      <li style="left:565px">LIVING ROOM <svg viewBox="0 0 10 10" aria-hidden="true"><path d="M1.5 3 L5 6.5 L8.5 3" fill="none" stroke="#fff" stroke-width="1.6"/></svg></li>
      <li style="left:793px">DINING ROOM <svg viewBox="0 0 10 10" aria-hidden="true"><path d="M1.5 3 L5 6.5 L8.5 3" fill="none" stroke="#fff" stroke-width="1.6"/></svg></li>
      <li style="left:1006px">CONTACT <svg viewBox="0 0 10 10" aria-hidden="true"><path d="M1.5 3 L5 6.5 L8.5 3" fill="none" stroke="#fff" stroke-width="1.6"/></svg></li>
    </ul>
  </nav>

  <section class="hero">
    <div class="hero-photo-left" role="img" aria-label="Dark mirrored dressing table with ornate mirror, vases and an upholstered stool"></div>
    <div class="hero-photo-right" role="img" aria-label="Bedroom with a tall upholstered headboard, grey bedding, cushions, a mirrored bedside table and lamp"></div>

    <svg class="hero-veil" viewBox="0 0 1200 355" aria-hidden="true">
      <defs>
        <path id="heart" d="M0 30 C-40 0 -30 -30 0 -14 C30 -30 40 0 0 30 Z"/>
      </defs>
      <path d="M0 0 H600 C665 110 665 245 590 355 H0 Z" fill="var(--maroon-veil)"/>
      <path d="M600 0 C665 110 665 245 590 355" fill="none" stroke="var(--sand)" stroke-opacity="0.45" stroke-width="1.5"/>
      <g fill="var(--heart-glow)">
        <use href="#heart" transform="translate(470 150) scale(4.2)"/>
        <use href="#heart" transform="translate(90 80) scale(1.6)"/>
        <use href="#heart" transform="translate(560 300) scale(1.3)"/>
        <use href="#heart" transform="translate(70 280) scale(1.1)"/>
      </g>
    </svg>

    <div class="hero-copy">
      <p class="hero-kicker">Find a Look You</p>
      <h1 class="hero-title">LOVE</h1>
      <p class="hero-text">Lorem ipsum dolor sit amet, consectetur elit.<br>Nam hendrerit nisi ac lacinia cursus.</p>
      <div class="hero-button">SHOP NOW</div>
    </div>
  </section>
</div>
</body>
</html>
```